Flyer for home based dog grooming salon

I need a flyer design for my home based dog grooming business. This flyer will be used for letterbox drops and supplied to local businesses such as vets. I may also extend the design at a later date for business cards as well.
Key advantages I want highlighted are listed below. They are listed in order of importance so that if the flyer becomes too busy, the less important items can be left off:
- "one on one personalised service where the groomer listens to your needs"
- NO CAGING...pets groomed immediately
- the same groomer for your pet at each groom, making your pet more comfortable
- local business in Alder Heights
- modern, air-conditioned salon
- VIP program offering discounts for regular clients
List of services to be included are listed below:
- tidy-ups
- full-body clipping
- strip-outs
- breed specific clips
- and more...
Phone number, website and email address all need to be indicated clearly so they stand out
0455 862 914 (use the spacing as shown)
www.marlowfieldtrims.com.au
info@marlowfieldtrims.com.au
I have no strong preferences for colours, however, as I am a male groomer, I don't want the flyer to be too feminine but also not too masculine as many of the prospective customers are female.
I have seen good examples of flyers with images of dogs being groomed on them and flyers with just images of dogs on them and I have no preference for either - it will depend on the overall look of the flyer. If you wish to include images of dogs being groomed, I have uploaded 38 images of dogs being groomed taken from my salon. I don't want images of anyone else grooming dogs on the flyer. As i cater to all size dogs, any images of dogs do not need to limited to small breeds.
The flyer size will be DL (99 x 210 mm) and can be single or double sided. If you plan on doing double sided, please ensure the list of services offered is shown on the front side.
As an example of several designs I have seen before, in 2012 there was a project for Hollisvale Groomers. From designs submitted, I liked #1135917, #1137543, #1135911 and probably would have gone for #1140593. I did not like the winner.
Dog owners
Salon

```html
<!DOCTYPE html>
<html lang="en">
<head>
<meta charset="utf-8">
<title>Home Based Dog Grooming Salon – Flyer</title>
<link href="https://fonts.googleapis.com/css2?family=Arimo:wght@400;700&family=Fira+Sans:ital,wght@0,400;0,500;0,700;1,600&display=swap" rel="stylesheet">
<style>
  :root {
    --stage: #e7e4df;
    --paper: #ffffff;
    --ink: #1d1d1d;
    --green: #6fcf3a;
    --green-dark: #3fa52a;
    --lime: #d6e83a;
    --orange: #f2a20c;
    --quote-orange: #d9620f;
    --service-orange: #ffb21a;
    --red: #e23a3c;
    --photo-light: #e9ecee;
    --photo-mid: #b7bcc0;
    --photo-dark: #3a3a3c;
  }
  * { box-sizing: border-box; margin: 0; padding: 0; }
  html, body { width: 904px; height: 1200px; overflow: hidden; }
  body { background: var(--stage); position: relative; font-family: "Fira Sans", sans-serif; }

  .flyer {
    position: absolute; left: 182px; top: 27px; width: 540px; height: 1146px;
    background: linear-gradient(180deg, var(--paper) 0%, #f4f5f5 60%, #eef0f0 100%);
    overflow: hidden; box-shadow: 0 4px 14px rgba(0,0,0,.18);
  }

  .header { position: absolute; top: 14px; left: 0; width: 100%; text-align: center; z-index: 3; }
  .header__kicker { font-family: "Arimo", sans-serif; font-size: 33px; color: var(--ink); line-height: 1.1; }
  .header__title {
    font-family: "Arimo", sans-serif; font-weight: 700; font-size: 37px; color: var(--green);
    letter-spacing: .5px; line-height: 1.2; text-shadow: 0 1px 1px rgba(0,0,0,.15);
  }

  .hero-photo {
    position: absolute; top: 104px; left: 0; width: 100%; height: 380px;
    background: linear-gradient(100deg, #f3f3f1 0%, #dfe2e3 35%, var(--photo-mid) 60%, var(--photo-dark) 85%, #2a2a2c 100%);
  }
  .hero-swoosh { position: absolute; top: 260px; left: 0; width: 540px; height: 230px; z-index: 1; }

  .faint-photo {
    position: absolute; top: 490px; left: 180px; width: 360px; height: 320px;
    background: radial-gradient(ellipse at 50% 40%, rgba(200,200,200,.45), rgba(255,255,255,0) 70%);
  }

  .photo-circle {
    position: absolute; border-radius: 50%; border: 7px solid #fff; z-index: 2;
    box-shadow: 0 0 0 3px #2b2b2b, 0 4px 10px rgba(0,0,0,.35);
  }
  .photo-circle--dog { left: 55px; top: 330px; width: 178px; height: 178px;
    background: radial-gradient(circle at 50% 45%, #f1ead8 0%, #d8cdb3 45%, #4b4b4b 100%); }
  .photo-circle--groom { left: 283px; top: 307px; width: 178px; height: 178px;
    background: radial-gradient(circle at 40% 45%, #e8e6e2 0%, #b9aba0 40%, #3a3a3c 100%); }
  .photo-circle--table { left: 350px; top: 695px; width: 142px; height: 142px;
    background: radial-gradient(circle at 60% 50%, #e4d3bf 0%, #b56a3a 40%, #2f2f30 100%); }

  .services {
    position: absolute; left: 16px; top: 540px; width: 253px; height: 256px;
    background: var(--red); border-radius: 0 0 14px 14px; z-index: 2;
    box-shadow: 0 3px 8px rgba(0,0,0,.3); text-align: center; padding-top: 16px;
  }
  .services__title { font-family: "Arimo", sans-serif; font-weight: 700; font-size: 36px; color: var(--green); margin-bottom: 6px; }
  .services__list { list-style: none; }
  .services__item { font-size: 23px; color: var(--service-orange); line-height: 35px; }
  .paw { width: 17px; height: 17px; vertical-align: -1px; margin-right: 3px; }

  .quote {
    position: absolute; right: 16px; top: 518px; width: 250px; z-index: 2;
    font-weight: 600; font-style: italic; font-size: 24px; line-height: 33px;
    color: var(--quote-orange); text-align: right;
  }

  .benefits {
    position: absolute; left: 16px; top: 842px; width: 510px; height: 197px;
    border-radius: 14px; z-index: 2; padding: 14px 16px 0 14px;
    background: linear-gradient(90deg, var(--green-dark) 0%, var(--lime) 45%, var(--green) 80%, var(--green-dark) 100%);
    box-shadow: 0 0 0 3px #fff, 0 3px 9px rgba(0,0,0,.3);
  }
  .benefits__list { list-style: none; }
  .benefits__item {
    position: relative; padding-left: 25px; font-family: "Arimo", sans-serif;
    font-size: 18.5px; line-height: 27px; color: var(--ink);
  }
  .benefits__item::before {
    content: ""; position: absolute; left: 2px; top: 8px;
    border-left: 13px solid var(--orange); border-top: 6px solid transparent; border-bottom: 6px solid transparent;
  }

  .contact { position: absolute; left: 0; top: 1044px; width: 100%; text-align: center; z-index: 2; }
  .contact__line { font-family: "Arimo", sans-serif; font-weight: 700; color: var(--ink); line-height: 33px; }
  .contact__line--phone { font-size: 25px; }
  .contact__line--web, .contact__line--mail { font-size: 23px; }
  .contact__icon { width: 17px; height: 17px; vertical-align: -1px; margin-right: 4px; }
</style>
</head>
<body>
<svg width="0" height="0" style="position:absolute">
  <defs>
    <symbol id="paw" viewBox="0 0 20 20">
      <circle cx="4" cy="8" r="2.4" fill="currentColor"/>
      <circle cx="8" cy="4" r="2.4" fill="currentColor"/>
      <circle cx="12.5" cy="4" r="2.4" fill="currentColor"/>
      <circle cx="16.5" cy="8" r="2.4" fill="currentColor"/>
      <ellipse cx="10.2" cy="13.8" rx="5" ry="4.2" fill="currentColor"/>
    </symbol>
  </defs>
</svg>

<main class="flyer">
  <header class="header">
    <div class="header__kicker">Home based</div>
    <h1 class="header__title">DOG GROOMING SALON</h1>
  </header>

  <div class="hero-photo" role="img" aria-label="Groomer smiling beside a freshly clipped white standard poodle in the salon"></div>

  <svg class="hero-swoosh" viewBox="0 0 540 230" aria-hidden="true">
    <path d="M0,180 C170,165 380,110 540,60 L540,230 L0,230 Z" fill="#ffffff"/>
    <path d="M0,128 C170,118 380,65 540,18 L540,48 C380,95 170,150 0,160 Z" fill="var(--green)"/>
    <path d="M0,160 C170,150 380,95 540,48 L540,62 C380,110 170,166 0,180 Z" fill="var(--orange)"/>
  </svg>

  <div class="faint-photo" role="img" aria-label="Faint background photo of a dog on the grooming table"></div>

  <div class="photo-circle photo-circle--dog" role="img" aria-label="Small fluffy dog after a tidy-up"></div>
  <div class="photo-circle photo-circle--groom" role="img" aria-label="Groomer trimming a small dog's face"></div>
  <div class="photo-circle photo-circle--table" role="img" aria-label="Groomer clipping a brown and white dog on the table"></div>

  <section class="services">
    <h2 class="services__title">SERVICES</h2>
    <ul class="services__list">
      <li class="services__item"><svg class="paw" style="color:#fff"><use href="#paw"/></svg>Tidy-ups</li>
      <li class="services__item"><svg class="paw" style="color:#fff"><use href="#paw"/></svg>Full-body clipping</li>
      <li class="services__item"><svg class="paw" style="color:#fff"><use href="#paw"/></svg>Strip-outs</li>
      <li class="services__item"><svg class="paw" style="color:#fff"><use href="#paw"/></svg>Breed specific clips</li>
      <li class="services__item"><svg class="paw" style="color:#fff"><use href="#paw"/></svg>and more...</li>
    </ul>
  </section>

  <p class="quote">"one on one personalised service where the groomer listens to your needs"</p>

  <section class="benefits">
    <ul class="benefits__list">
      <li class="benefits__item">NO CAGING...pets groomed immediately</li>
      <li class="benefits__item">the same groomer for your pet at each groom, making your pet more comfortable</li>
      <li class="benefits__item">local business in Alder Heights</li>
      <li class="benefits__item">modern, air-conditioned salon</li>
      <li class="benefits__item">VIP program offering discounts for regular clients</li>
    </ul>
  </section>

  <footer class="contact">
    <div class="contact__line contact__line--phone">
      <svg class="contact__icon" viewBox="0 0 20 20" aria-hidden="true"><rect width="20" height="20" rx="4" fill="var(--green)"/><path d="M6.5 4.5l2 2.6-1.2 1.3c.8 1.7 2 2.9 3.6 3.7l1.3-1.2 2.6 2-1.3 2c-4.2-.3-8.6-4.6-8.9-8.9z" fill="#fff"/></svg>0455 862 914
    </div>
    <div class="contact__line contact__line--web">
      <svg class="contact__icon" viewBox="0 0 20 20" aria-hidden="true"><circle cx="10" cy="10" r="8.5" fill="none" stroke="var(--green)" stroke-width="1.8"/><ellipse cx="10" cy="10" rx="3.6" ry="8.5" fill="none" stroke="var(--green)" stroke-width="1.5"/><path d="M1.5 10h17M3 5.5h14M3 14.5h14" stroke="var(--green)" stroke-width="1.3"/></svg>www.marlowfieldtrims.com.au
    </div>
    <div class="contact__line contact__line--mail">
      <svg class="contact__icon" viewBox="0 0 20 20" aria-hidden="true"><rect x="1" y="4" width="18" height="12" rx="1.5" fill="var(--green)"/><path d="M1.5 4.8l8.5 6.4 8.5-6.4" fill="none" stroke="#fff" stroke-width="1.5"/></svg>info@marlowfieldtrims.com.au
    </div>
  </footer>
</main>
</body>
</html>
```